Cyber Security Company Services Graphic

We need a 3D graphic of our services that resembles a great graphic that is used by another company. The image will be used on web sites, in presentations, and collateral. We will need to modify the text at some point as we change the name of the services. The attached file has the content that needs to be in our graphic (rough layout) and the example of a great graphic that we are using as the baseline for our image.

```html
<!DOCTYPE html>
<html lang="en">
<head>
<meta charset="utf-8">
<title>Integrated Cyber Services Graphic</title>
<link href="https://fonts.googleapis.com/css2?family=Lato:wght@300;700;900&display=swap" rel="stylesheet">
<style>
  :root{
    --navy:#1b2440;
    --navy-ink:#1c2545;
    --title:#e6e8ee;
    --orange:#f66b35;
    --orange-top:#ee5a22;
    --orange-side:#c9461b;
    --pennant:#f2612a;
    --pennant-edge:#d24b1c;
    --slab-top:#c9ccd3;
    --slab-front:#ffffff;
  }
  html,body{margin:0;padding:0;overflow:hidden;}
  body{width:1200px;height:675px;background:var(--navy);font-family:'Lato',sans-serif;}
  .canvas{position:relative;width:1200px;height:675px;overflow:hidden;background:var(--navy);}
  .title{position:absolute;right:22px;top:14px;margin:0;text-align:right;color:var(--title);
    font-size:42px;line-height:44px;letter-spacing:2px;font-weight:300;}
  .title strong{font-weight:900;display:block;}
  .title span{display:block;}
  .stack{position:absolute;left:0;top:0;}
  .layer-label{font-family:'Lato',sans-serif;font-weight:900;fill:var(--navy-ink);letter-spacing:4.5px;font-size:17px;text-anchor:middle;}
  .block-label{font-family:'Lato',sans-serif;font-weight:900;fill:var(--navy-ink);font-size:10.5px;text-anchor:middle;}
  .pennant-label{font-family:'Lato',sans-serif;font-weight:900;fill:var(--navy-ink);font-size:5.6px;text-anchor:middle;}
  .icon{fill:var(--navy-ink);stroke:none;}
  .icon-line{fill:none;stroke:var(--navy-ink);stroke-width:1.6;}
  .pennant-body{fill:var(--pennant);}
  .pennant-side{fill:var(--pennant-edge);}
  .face-top{fill:var(--orange-top);}
  .face-front{fill:var(--orange);}
  .face-side{fill:var(--orange-side);}
</style>
</head>
<body>
<div class="canvas">
  <h1 class="title"><span>INTEGRATED</span><strong>CYBER</strong><strong>SERVICES</strong><span>GRAPHIC</span></h1>

  <svg class="stack" width="1200" height="675" viewBox="0 0 1200 675" xmlns="http://www.w3.org/2000/svg">
    <defs>
      <linearGradient id="slabTop" x1="0" y1="0" x2="0" y2="1">
        <stop offset="0" stop-color="#9a9ea8"/>
        <stop offset="1" stop-color="#e9eaed"/>
      </linearGradient>
      <linearGradient id="orangeTop" x1="0" y1="0" x2="0" y2="1">
        <stop offset="0" stop-color="#c8441a"/>
        <stop offset="1" stop-color="#f05a20"/>
      </linearGradient>
    </defs>

    <!-- Base: portal & operating system -->
    <g class="base-slab">
      <polygon points="195,468 1016,468 1109,552 95,552" fill="url(#slabTop)"/>
      <rect x="95" y="552" width="1014" height="30" fill="var(--slab-front)"/>
      <text class="layer-label" x="602" y="577">KELVORA PORTAL &amp; OPERATING SYSTEM</text>
    </g>

    <!-- Lower service blocks -->
    <g class="support-blocks">
      <polygon points="188,469 391,469 354,492 164,492" fill="url(#orangeTop)"/>
      <polygon points="354,492 391,469 391,498 354,521" class="face-side"/>
      <rect x="164" y="492" width="190" height="29" class="face-front"/>
      <text class="block-label" x="259" y="511">CONSULTING &amp; ADVISORY</text>

      <polygon points="396,469 588,469 583,492 391,492" fill="url(#orangeTop)"/>
      <polygon points="583,492 588,469 588,498 583,521" class="face-side"/>
      <rect x="391" y="492" width="192" height="29" class="face-front"/>
      <text class="block-label" x="487" y="511">MARKETING &amp; SALES</text>

      <polygon points="616,469 800,469 811,492 620,492" fill="url(#orangeTop)"/>
      <polygon points="616,469 620,492 620,521 616,498" class="face-side"/>
      <rect x="620" y="492" width="191" height="29" class="face-front"/>
      <text class="block-label" x="715" y="511">REPORTS &amp; COMPLIANCE</text>

      <polygon points="821,469 1016,469 1044,492 850,492" fill="url(#orangeTop)"/>
      <polygon points="821,469 850,492 850,521 821,498" class="face-side"/>
      <rect x="850" y="492" width="194" height="29" class="face-front"/>
      <text class="block-label" x="947" y="511">TRAINING</text>
    </g>

    <!-- Middle: managed security services -->
    <g class="managed-slab">
      <polygon points="230,419 980,419 1016,442 195,442" fill="url(#slabTop)"/>
      <rect x="195" y="442" width="821" height="27" fill="var(--slab-front)"/>
      <text class="layer-label" x="606" y="463">MANAGED SECURITY SERVICES</text>
    </g>

    <!-- Upper pillar blocks -->
    <g class="pillar-blocks">
      <polygon points="275,369 494,369 475,397 230,397" fill="url(#orangeTop)"/>
      <polygon points="475,397 494,369 494,393 475,421" class="face-side"/>
      <rect x="230" y="397" width="245" height="24" class="face-front"/>
      <text class="block-label" x="353" y="413">VULNERABILITY MANAGEMENT</text>

      <polygon points="497,369 722,369 728,397 481,397" fill="url(#orangeTop)"/>
      <rect x="481" y="397" width="247" height="24" class="face-front"/>
      <text class="block-label" x="601" y="413">24X7 CONTINUOUS DETECTION &amp; RESPONSE</text>

      <polygon points="722,369 931,369 980,397 734,397" fill="url(#orangeTop)"/>
      <polygon points="722,369 734,397 734,421 722,393" class="face-side"/>
      <rect x="734" y="397" width="246" height="24" class="face-front"/>
      <text class="block-label" x="857" y="413">GOVERNANCE, RISK, &amp; COMPLIANCE</text>
    </g>

    <!-- Pennants -->
    <g class="pennants">
      <g transform="translate(293,0)">
        <polygon class="pennant-side" points="-27,254 25,254 27,346 0,377 -25,346"/>
        <polygon class="pennant-body" points="-25,254 25,254 25,346 0,376 -25,346"/>
        <circle class="icon" cx="0" cy="290" r="10"/>
        <text class="pennant-label" x="0" y="331">HUMAN</text>
        <text class="pennant-label" x="0" y="338">BEHAVIOUR</text>
      </g>
      <g transform="translate(348,0)">
        <polygon class="pennant-side" points="-27,254 25,254 27,346 0,377 -25,346"/>
        <polygon class="pennant-body" points="-25,254 25,254 25,346 0,376 -25,346"/>
        <text class="pennant-label" x="0" y="277">THREAT</text>
        <text class="pennant-label" x="0" y="284">HUNTING</text>
        <rect class="icon" x="-14" y="315" width="28" height="28"/>
        <circle cx="0" cy="329" r="5" fill="var(--pennant)"/>
      </g>
      <g transform="translate(402,0)">
        <polygon class="pennant-side" points="-27,254 25,254 27,346 0,377 -25,346"/>
        <polygon class="pennant-body" points="-25,254 25,254 25,346 0,376 -25,346"/>
        <rect class="icon" x="-14" y="276" width="28" height="28" rx="1"/>
        <rect x="-12" y="281" width="24" height="21" fill="var(--pennant)"/>
        <path class="icon" d="M0,284 l6,2 v5 q0,6 -6,8 q-6,-2 -6,-8 v-5z"/>
        <text class="pennant-label" x="0" y="331">VULNERABILITY</text>
        <text class="pennant-label" x="0" y="338">ASSESSMENT</text>
      </g>
      <g transform="translate(457,0)">
        <polygon class="pennant-side" points="-27,254 25,254 27,346 0,377 -25,346"/>
        <polygon class="pennant-body" points="-25,254 25,254 25,346 0,376 -25,346"/>
        <text class="pennant-label" x="0" y="277">VULNERABILITY</text>
        <text class="pennant-label" x="0" y="284">MANAGEMENT</text>
        <circle class="icon" cx="0" cy="330" r="14"/>
        <circle cx="0" cy="330" r="9" fill="none" stroke="var(--pennant)" stroke-width="1.6"/>
        <circle cx="0" cy="330" r="3.5" fill="var(--pennant)"/>
        <path d="M0,330 L10,320" stroke="var(--pennant)" stroke-width="1.6"/>
      </g>
      <g transform="translate(524,0)">
        <polygon class="pennant-side" points="-27,254 25,254 27,346 0,377 -25,346"/>
        <polygon class="pennant-body" points="-25,254 25,254 25,346 0,376 -25,346"/>
        <path class="icon" d="M0,276 l11,4 v10 q0,10 -11,14 q-11,-4 -11,-14 v-10z"/>
        <path d="M-4,286 l8,8 M4,286 l-8,8" stroke="var(--pennant)" stroke-width="1.8"/>
        <text class="pennant-label" x="0" y="331">ENDPOINT</text>
        <text class="pennant-label" x="0" y="338">PROTECTION</text>
      </g>
      <g transform="translate(579,0)">
        <polygon class="pennant-side" points="-27,254 25,254 27,346 0,377 -25,346"/>
        <polygon class="pennant-body" points="-25,254 25,254 25,346 0,376 -25,346"/>
        <text class="pennant-label" x="0" y="277">NETWORKS &amp;</text>
        <text class="pennant-label" x="0" y="284">SERVERS</text>
        <rect class="icon" x="-14" y="324" width="28" height="19"/>
        <path d="M-14,325 L0,335 L14,325" stroke="var(--pennant)" stroke-width="1.6" fill="none"/>
        <rect class="icon" x="2" y="315" width="4" height="7"/>
      </g>
      <g transform="translate(634,0)">
        <polygon class="pennant-side" points="-27,254 25,254 27,346 0,377 -25,346"/>
        <polygon class="pennant-body" points="-25,254 25,254 25,346 0,376 -25,346"/>
        <path class="icon" d="M-12,298 a6,6 0 0 1 1,-12 a8,8 0 0 1 15,-3 a6,6 0 0 1 9,6 a5,5 0 0 1 -1,9z"/>
        <rect x="-3" y="289" width="6" height="5" fill="var(--pennant)"/>
        <text class="pennant-label" x="0" y="335">CLOUD</text>
      </g>
      <g transform="translate(689,0)">
        <polygon class="pennant-side" points="-27,254 25,254 27,346 0,377 -25,346"/>
        <polygon class="pennant-body" points="-25,254 25,254 25,346 0,376 -25,346"/>
        <text class="pennant-label" x="0" y="277">24X7</text>
        <text class="pennant-label" x="0" y="284">SOC</text>
        <rect class="icon" x="-14" y="315" width="28" height="28"/>
        <text x="0" y="329" text-anchor="middle" font-family="Lato,sans-serif" font-weight="900" font-size="7" fill="var(--pennant)">0101</text>
        <text x="0" y="339" text-anchor="middle" font-family="Lato,sans-serif" font-weight="900" font-size="7" fill="var(--pennant)">1010</text>
      </g>
      <g transform="translate(757,0)">
        <polygon class="pennant-side" points="-27,254 25,254 27,346 0,377 -25,346"/>
        <polygon class="pennant-body" points="-25,254 25,254 25,346 0,376 -25,346"/>
        <rect class="icon-line" x="-10" y="280" width="20" height="20"/>
        <rect class="icon" x="-5" y="285" width="10" height="10"/>
        <path class="icon-line" d="M-6,276v4 M0,276v4 M6,276v4 M-6,300v4 M0,300v4 M6,300v4 M-14,284h4 M-14,290h4 M-14,296h4 M10,284h4 M10,290h4 M10,296h4"/>
        <text class="pennant-label" x="0" y="335">TECHNOLOGY</text>
      </g>
      <g transform="translate(811,0)">
        <polygon class="pennant-side" points="-27,254 25,254 27,346 0,377 -25,346"/>
        <polygon class="pennant-body" points="-25,254 25,254 25,346 0,376 -25,346"/>
        <text class="pennant-label" x="0" y="281">PEOPLE</text>
        <circle class="icon" cx="0" cy="329" r="14"/>
        <circle cx="0" cy="325" r="4" fill="none" stroke="var(--pennant)" stroke-width="1.6"/>
        <path d="M-7,338 q7,-10 14,0" fill="none" stroke="var(--pennant)" stroke-width="1.6"/>
      </g>
      <g transform="translate(866,0)">
        <polygon class="pennant-side" points="-27,254 25,254 27,346 0,377 -25,346"/>
        <polygon class="pennant-body" points="-25,254 25,254 25,346 0,376 -25,346"/>
        <rect class="icon" x="-6" y="276" width="12" height="7"/>
        <path class="icon-line" d="M0,283v5 M-10,294h20 M-10,294v5 M10,294v5"/>
        <path class="icon" d="M0,288 l5,5 l-5,5 l-5,-5z"/>
        <rect class="icon" x="-13" y="298" width="7" height="7"/>
        <circle class="icon" cx="10" cy="302" r="3.5"/>
        <text class="pennant-label" x="0" y="335">PROCESS</text>
      </g>
      <g transform="translate(921,0)">
        <polygon class="pennant-side" points="-27,254 25,254 27,346 0,377 -25,346"/>
        <polygon class="pennant-body" points="-25,254 25,254 25,346 0,376 -25,346"/>
        <text class="pennant-label" x="0" y="277">CYBER</text>
        <text class="pennant-label" x="0" y="284">INSURANCE</text>
        <path class="icon-line" stroke-dasharray="2 2" d="M-12,318h24 M-12,341h24 M10,318L-10,341"/>
        <circle class="icon" cx="-12" cy="318" r="2.4"/>
        <circle class="icon" cx="0" cy="318" r="2.4"/>
        <circle class="icon" cx="12" cy="318" r="2.4"/>
        <circle class="icon" cx="0" cy="329" r="2.4"/>
        <circle class="icon" cx="-12" cy="341" r="2.4"/>
        <circle class="icon" cx="0" cy="341" r="2.4"/>
        <circle class="icon" cx="12" cy="341" r="2.4"/>
      </g>
    </g>
  </svg>
</div>
</body>
</html>
```